Design a modern, premium front panel for a stand-up pouch

Design a modern, premium front for a stand-up pouch for VELUTRA. Product is for Urine/vomit/runny stool incidents indoors; quick cleanups before smell sets; nighttime/elderly pet accidents; travel/car mishaps.

It must instantly show it’s for dogs & cats and include three small step icons with labels: Sprinkle → Wait 1–5 min → Sweep. Front copy to include: VELUTRA, descriptor “Mineral Instant Absorber – for Dogs & Cats”, one benefits line “Fragrance-Free • 100 % Mineral • Odor-Binding • Low-Dust

Goal: clear who/what/how in under 3 seconds
Deliverables: AI/PDF + a pouch mockup;

Target Market(s)

• Dog & cat households in apartments/homes; new pet parents, senior pets, multi-pet homes. • Cleanliness & odor-sensitive buyers (allergies/asthma, fragrance-free preference). • Surfaces at risk: carpets/rugs, sofas, mattresses, car interiors.

Industry/Entity Type

Pet e-commerce and retail

Font styles to use
Other font styles liked:
• like attached images

Requirements
Nice to have
• light background, eco friendly

```html
<!DOCTYPE html>
<html lang="en">
<head>
<meta charset="utf-8">
<title>VELUTRA – Mineral Instant Absorber Pouch Front</title>
<link href="https://fonts.googleapis.com/css2?family=Raleway:wght@300&family=Montserrat:wght@600;700&display=swap" rel="stylesheet">
<style>
  :root {
    --backdrop: #e4e4e4;
    --pouch-top: #b2d136;
    --pouch-mid: #cfe27a;
    --pouch-pale: #f4f8e6;
    --pouch-bottom: #dcebab;
    --brand-white: #ffffff;
    --ink: #1f2a14;
    --ink-soft: #3a3f33;
    --step-green: #2f9a3a;
    --sticker-blue: #2a62d4;
    --sticker-pale: #dfe8fb;
  }
  * { box-sizing: border-box; margin: 0; padding: 0; }
  html, body { width: 1200px; height: 1200px; overflow: hidden; }
  body {
    background: var(--backdrop);
    font-family: "Montserrat", Arial, sans-serif;
    position: relative;
  }
  .pouch {
    position: absolute;
    left: 333px; top: 124px;
    width: 531px; height: 915px;
    border-radius: 10px 10px 6px 6px;
    background: linear-gradient(180deg,
      var(--pouch-top) 0%,
      var(--pouch-top) 24%,
      var(--pouch-mid) 44%,
      var(--pouch-pale) 58%,
      #ffffff 70%,
      var(--pouch-pale) 86%,
      var(--pouch-bottom) 100%);
    overflow: hidden;
    box-shadow: 0 18px 40px rgba(0,0,0,0.12);
  }
  .zipper-line {
    position: absolute; left: 0; right: 0; height: 3px;
    background: rgba(120,150,20,0.35);
    box-shadow: 0 1px 0 rgba(255,255,255,0.45);
  }
  .zipper-line.upper { top: 90px; }
  .zipper-line.lower { top: 112px; }
  .tear-notch {
    position: absolute; top: 56px; width: 10px; height: 10px;
    background: var(--backdrop); border-radius: 50%;
  }
  .tear-notch.left { left: -5px; }
  .tear-notch.right { right: -5px; }
  .brand-name {
    position: absolute; top: 152px; left: 0; right: 0;
    text-align: center;
    font-family: "Raleway", Arial, sans-serif;
    font-weight: 300;
    font-size: 70px; letter-spacing: 3px;
    color: var(--brand-white);
    line-height: 1;
  }
  .descriptor {
    position: absolute; top: 238px; left: 0; right: 0;
    text-align: center;
    font-weight: 700; font-size: 19px; line-height: 30px;
    letter-spacing: 0.3px;
    color: var(--ink);
  }
  .steps {
    position: absolute; top: 325px; left: 0; right: 0;
    display: flex; justify-content: center; gap: 24px;
  }
  .step { width: 104px; text-align: center; }
  .step svg { width: 96px; height: 96px; display: block; margin: 0 auto; }
  .step-label {
    margin-top: 10px;
    font-weight: 700; font-size: 15px;
    color: var(--step-green);
  }
  .benefits {
    position: absolute; top: 478px; left: 112px;
    display: grid; grid-template-columns: 170px 160px;
    column-gap: 8px; row-gap: 2px;
    list-style: none;
    font-weight: 700; font-size: 16px;
    color: var(--ink-soft);
  }
  .benefits li::before { content: "•"; margin-right: 8px; }
  .pets-photo {
    position: absolute; left: 68px; top: 536px;
    width: 440px; height: 311px;
    background: radial-gradient(ellipse at 32% 58%, #b97a3e 0%, #c99565 26%, rgba(240,240,232,0) 52%),
                radial-gradient(ellipse at 72% 45%, #3a2c22 0%, #8a6a50 24%, rgba(240,240,232,0) 50%),
                linear-gradient(180deg, rgba(240,242,236,0.4), rgba(226,238,200,0.8));
  }
  .goal-sticker {
    position: absolute; left: 45px; top: 559px;
    width: 100px; height: 100px;
    border-radius: 12px;
    background: linear-gradient(135deg, var(--sticker-blue) 0%, var(--sticker-pale) 100%);
    opacity: 0.85;
  }
</style>
</head>
<body>
  <main class="pouch" aria-label="VELUTRA stand-up pouch front panel">
    <span class="tear-notch left"></span>
    <span class="tear-notch right"></span>
    <div class="zipper-line upper"></div>
    <div class="zipper-line lower"></div>

    <h1 class="brand-name">VELUTRA</h1>
    <p class="descriptor">MINERAL INSTANT ABSORBER<br>FOR DOGS &amp; CATS</p>

    <section class="steps">
      <div class="step">
        <svg viewBox="0 0 108 108" fill="none" stroke="var(--step-green)" stroke-width="3" stroke-linecap="round" stroke-linejoin="round">
          <circle cx="54" cy="54" r="50"/>
          <path d="M58 26 L40 54 L48 58 L66 32"/>
          <path d="M66 32 Q74 30 72 40 L60 58"/>
          <g fill="var(--step-green)" stroke="none">
            <circle cx="44" cy="66" r="2.4"/><circle cx="52" cy="66" r="2.4"/>
            <circle cx="40" cy="74" r="2.4"/><circle cx="48" cy="74" r="2.4"/><circle cx="56" cy="74" r="2.4"/>
            <circle cx="44" cy="82" r="2.4"/><circle cx="52" cy="82" r="2.4"/>
          </g>
        </svg>
        <p class="step-label">Sprinkle</p>
      </div>
      <div class="step">
        <svg viewBox="0 0 108 108" fill="none" stroke="var(--step-green)" stroke-width="3" stroke-linecap="round" stroke-linejoin="round">
          <circle cx="54" cy="54" r="50"/>
          <circle cx="58" cy="58" r="22"/>
          <path d="M58 44 V58 L67 63"/>
          <path d="M54 32 H62 M58 32 V36"/>
          <path d="M74 40 L78 36"/>
          <path d="M24 50 H32 M20 58 H30 M24 66 H32"/>
        </svg>
        <p class="step-label">Wait 1-5 min</p>
      </div>
      <div class="step">
        <svg viewBox="0 0 108 108" fill="none" stroke="var(--step-green)" stroke-width="3" stroke-linecap="round" stroke-linejoin="round">
          <circle cx="54" cy="54" r="50"/>
          <path d="M34 24 L58 60"/>
          <path d="M50 58 L66 52 L74 74 L40 80 Z"/>
          <path d="M52 66 L48 78 M60 64 L58 77 M67 62 L67 75"/>
          <circle cx="80" cy="76" r="5"/><circle cx="86" cy="70" r="3"/>
          <path d="M70 28 V36 M66 32 H74"/>
        </svg>
        <p class="step-label">Sweep</p>
      </div>
    </section>

    <ul class="benefits">
      <li>Fragrance-Free</li>
      <li>Odor-Binding</li>
      <li>100 % Mineral</li>
      <li>Low-Dust</li>
    </ul>

    <div class="pets-photo" role="img" aria-label="Photo of a tabby cat and a tricolour dog lying side by side on a light background"></div>

    <div class="goal-sticker" role="img" aria-label="Blue stopwatch sticker graphic"></div>
  </main>
</body>
</html>
```